AN ELEGANT COSMETIC LABLE THAT CAN EASILY BE ALTERED TO FIT A VARIETY OF DIFFERENT PRODUCTS.

Predictable and ordinary designs are NOT welcome. Creative minds wanted.

Looking for a professional lable that is Canadian/USA Standard and compliant with the Food and Drug - Cosmetic Act in Onatrio. Which has a clean and elegant look, with a hint of holistic vibes.

This lable should be sleak and flexible to be altered to fit a variety of different products. Let your creativity come out with this project, the crazy and unpredictable are welcome.

This lable may be on the next biggest Cosmetic brand in the world. If you can see it, you can design it. All the best, looking forward to working with you.

Target Market(s)

Everyone who is looking for a clean natural lifestyle. The elite crowd.

Industry/Entity Type

Cosmetics

Font styles to use
Serif
Script

Colors

Designer to choose only greyscale colors for use in the design.

Requirements
Must have
• Company Name " BRELLOW'S" and or Logo. See attachment
Nice to have
• One or more solid bars that can be colored to match the main product ingredient colour.
Should not have
• Too much different colors or images

```html
<!DOCTYPE html>
<html lang="en">
<head>
<meta charset="utf-8">
<title>Brellow's Aloe Vera Label</title>
<link href="https://fonts.googleapis.com/css2?family=Kumbh+Sans:wght@400;500;700;800&family=Great+Vibes&family=Rozha+One&display=swap" rel="stylesheet">
<style>
  :root{
    --leaf:#8cc63f;
    --leaf-dark:#2f7d3a;
    --ink:#111111;
    --paper:#ffffff;
    --mist:#e6ecdf;
    --sketch:#f1f1f1;
  }
  *{box-sizing:border-box;margin:0;padding:0}
  html,body{width:1200px;height:558px;overflow:hidden;background:var(--paper)}
  body{font-family:"Kumbh Sans",sans-serif;color:var(--ink)}
  .label{position:relative;width:1200px;height:558px;overflow:hidden;background:var(--paper)}
  .backdrop{position:absolute;inset:0;background:
      radial-gradient(ellipse at 20% 30%, var(--mist) 0%, rgba(255,255,255,0) 45%),
      radial-gradient(ellipse at 85% 20%, var(--mist) 0%, rgba(255,255,255,0) 45%),
      radial-gradient(ellipse at 75% 80%, var(--mist) 0%, rgba(255,255,255,0) 40%),
      radial-gradient(ellipse at 10% 85%, var(--mist) 0%, rgba(255,255,255,0) 40%)}
  .band-top{position:absolute;left:0;top:0;width:100%;height:19px;background:var(--leaf)}
  .band-bottom{position:absolute;left:0;bottom:0;width:100%;height:10px;background:var(--leaf)}

  .portrait{position:absolute;left:332px;top:190px;width:203px;height:355px;
      background:linear-gradient(160deg,var(--sketch) 0%,#e6e6e6 100%);border-radius:100px 100px 0 0}
  .ornament{position:absolute;left:452px;top:340px;width:383px;height:108px;border-radius:54px;
      background:radial-gradient(ellipse at center,rgba(140,198,63,.16) 0%,rgba(140,198,63,0) 70%)}

  .ingredients{position:absolute;left:24px;top:43px;font-size:15.4px;line-height:20px;text-align:justify;letter-spacing:.2px}
  .ingredients .en{width:284px}
  .ingredients .fr{width:300px;margin-top:6px}
  .heading{color:var(--leaf-dark);font-weight:500}

  .warnings{position:absolute;left:18px;top:304px;width:279px;border:2px solid var(--ink)}
  .warnings p{font-size:12.8px;line-height:17px;padding:4px 5px 0}
  .warnings .en{height:56px}
  .warnings .fr{height:60px;border-top:2px solid var(--ink);padding-top:5px}

  .claims{position:absolute;left:22px;top:429px;font-size:11.2px;font-weight:700;line-height:14.4px}
  .claims .gap{display:block;height:2px}

  .brand{position:absolute;left:420px;top:110px;width:290px;text-align:center;font-weight:800;font-size:46px;letter-spacing:1px;line-height:1}
  .tagline{position:absolute;left:445px;top:166px;width:240px;text-align:center;font-family:"Great Vibes",cursive;font-size:24px;line-height:1.1;word-spacing:6px}

  .product-name{position:absolute;left:498px;top:222px;width:250px;font-family:"Great Vibes",cursive;font-size:52px;line-height:1;white-space:nowrap}
  .product-name-fr{position:absolute;left:546px;top:288px;font-family:"Great Vibes",cursive;font-size:30px;line-height:1;white-space:nowrap}
  .ingredient-title{position:absolute;left:498px;top:335px;font-family:"Rozha One",serif;font-size:92px;line-height:1;color:var(--leaf);white-space:nowrap;transform:scaleX(.72);transform-origin:left top}

  .badges{position:absolute;left:541px;top:459px;display:flex;gap:8px}
  .badge{width:53px;height:53px;border-radius:50%;border:3px solid #333;background:#f2f2f2}
  .net-weight{position:absolute;left:586px;top:519px;font-size:17px}

  .details{position:absolute;left:856px;top:29px;width:325px;font-size:15.4px;line-height:20px;text-align:justify;letter-spacing:.2px}
  .details .fr{margin-top:27px}
  .maker{position:absolute;left:859px;top:410px;font-size:12.8px;font-weight:700;line-height:17px}
  .maker .web{display:block;margin-top:2px}

  .care-icons{position:absolute;left:850px;top:494px;display:flex;gap:12px;align-items:flex-end}
  .care-icons svg{display:block}
  .other{font-size:9.5px;font-weight:700;text-align:center}
  .expiry{position:absolute;left:1032px;top:489px;width:157px;height:46px;border:1.5px solid var(--ink);font-size:13px;text-align:center;padding-top:3px}
</style>
</head>
<body>
<main class="label">
  <div class="backdrop" role="img" aria-label="Faint pale green aloe leaf pattern across the background"></div>
  <div class="band-top"></div>
  <div class="band-bottom"></div>

  <div class="portrait" role="img" aria-label="Line illustration of a woman with a towel wrapped around her hair"></div>
  <div class="ornament" role="img" aria-label="Green decorative swirl flourishes framing the product title"></div>

  <section class="ingredients">
    <p class="en"><span class="heading">Ingredients:</span> Aloe gel, coconut oil, water, cetearyl alchohol, glycerin stearate, beeswax, dimethicon, phenoxyethanol, sodium polyacrylate, vitamin E.</p>
    <p class="fr"><span class="heading">Ingrédients:</span> Gel d’aloès, huile de nix de coco, eau, alcool cetearyl, glycérine, huile de tournesol, beurre de karité, stéarate de glycérine, cire d’abeille, diméthicone, phénoxyéthanol, polyacrylate de sodium, vitamine E.</p>
  </section>

  <section class="warnings">
    <p class="en"><strong>WARNING:</strong> This product is not intended for human consumption. If irritation occurs, discontinue use.</p>
    <p class="fr"><strong>ATTENTION:</strong> Ce produit n’est pas destiné à la consommation humaine. En cas d’irritation, cesser l’utilisation.</p>
  </section>

  <div class="claims">
    FRAGRANCE FREE | GLUTEN FREE |<br>PHTHALATE FREE | CRUELTY FREE
    <span class="gap"></span>
    SANS PARFUM | SANS GLUTEN |<br>SANS PHTALATE | SANS CRUAUTÉ
  </div>

  <div class="brand">BRELLOW'S</div>
  <div class="tagline">Made for you Faite pour vous</div>

  <div class="product-name">Skin Drencher</div>
  <div class="product-name-fr">Peau Drencher</div>
  <div class="ingredient-title">Aloe Vera</div>

  <div class="badges" aria-label="Product claim seals">
    <div class="badge"></div><div class="badge"></div><div class="badge"></div><div class="badge"></div>
  </div>
  <div class="net-weight">453.59 g/ 16 oz</div>

  <section class="details">
    <p class="en"><span class="heading">Details:</span> Luxuriously rich moisturizer that melts effortlessly into the skin, leaving it soft and luminous. This new and improved formulation is pH-optimized for glowing skin that remains hydrated and protected all day long. It leaves no sticky residues and is easy to spread while still maintaining the lock and feel of a premium product.</p>
    <p class="fr"><span class="heading">Détails:</span> Hydratant riche et luxueux qui fond sans effort dans la peau, la laissant douce et lumineuse. Cette nouvelle formulation améliorée a un pH optimisé pour une peau éclatante qui reste hydratée et protégée toute la journée. Il ne laisse aucun résidu collant et est facile à étaler tout en conservant l’apparence et la sensation d’un produit haut de gamme.</p>
  </section>

  <div class="maker">Produced by Brellow’s, Canada<br>Produit par Brellow's, Canada<span class="web">www.brellows.ca</span></div>

  <div class="care-icons">
    <svg width="34" height="36" viewBox="0 0 34 36" aria-label="Use within 6 months">
      <path d="M3 10 L26 2" stroke="#111" stroke-width="2" fill="none"/>
      <rect x="3" y="14" width="28" height="18" rx="3" fill="none" stroke="#111" stroke-width="2"/>
      <text x="17" y="29" font-family="Kumbh Sans,sans-serif" font-size="9" font-weight="700" text-anchor="middle">6 M</text>
    </svg>
    <svg width="30" height="34" viewBox="0 0 30 34" aria-label="Dispose in bin">
      <rect x="1" y="1" width="28" height="32" fill="none" stroke="#111" stroke-width="1.5"/>
      <rect x="6" y="15" width="10" height="13" fill="#111"/>
      <circle cx="21" cy="7" r="3" fill="#111"/>
      <path d="M19 11 L23 11 L24 27 L20 27 Z" fill="#111"/>
    </svg>
    <div>
      <svg width="36" height="32" viewBox="0 0 36 32" aria-label="Recycling code 7">
        <path d="M18 3 L33 28 L3 28 Z" fill="none" stroke="#111" stroke-width="2.5"/>
        <text x="18" y="24" font-family="Kumbh Sans,sans-serif" font-size="13" font-weight="700" text-anchor="middle">7</text>
      </svg>
      <div class="other">OTHER</div>
    </div>
    <svg width="36" height="36" viewBox="0 0 36 36" aria-label="Recyclable">
      <circle cx="18" cy="18" r="17" fill="#111"/>
      <path d="M10 18 A8 8 0 0 1 26 16" stroke="#fff" stroke-width="3" fill="none"/>
      <path d="M26 20 A8 8 0 0 1 10 20" stroke="#fff" stroke-width="3" fill="none"/>
    </svg>
  </div>

  <div class="expiry">Exp.Date/Date d'exp.</div>
</main>
</body>
</html>
```